RW Hollis LLC Business Card - Civil Engineering & Consulting Firm

We need a Business Card that is elegant, and masculine.  It is our Professional Civil Engineering & Consulting Company located in San Antonio TX (Not s construction or builder firm- no gears & no tool images please). We provide civil engineering services including  commercial site plans, grading and drainage plans, utility plans, hydraulics and hydrology, land planning, utility coordination, and other general civil engineering services related to commercial and residential development.
We have 2 existing Logos. We would like to convey reliability, strength, trustworthiness and attention to detail.  Blues and orange tones as per logo We are OK with the use of a darker blue in the mix.  We have 2 logo versions - Full Company Name Logo to go on the back of card, & Small Icon Logo for the front w/ personal Info.

Target Market(s)
Architects, Real Estate Developers, Other Strctural Engineers, Surveyers, General Contractors
Industry/Entity Type
Professional Civil Engineering
Contact Information for Business Card
Name, Position, Address, Cell & Office #, email, and company website
Font styles to use
Other font styles liked:
- Avian
Requirements
Should not have
- No Tools, No Gears, no Cranes, or Construction Equipment.

```html
<!DOCTYPE html>
<html lang="en">
<head>
<meta charset="utf-8">
<title>RW Hollis LLC Business Card</title>
<link href="https://fonts.googleapis.com/css2?family=Mulish:wght@400;700&display=swap" rel="stylesheet">
<style>
  :root {
    --backdrop: #1c1d20;
    --navy: #0b2444;
    --orange: #f0901e;
    --sky: #7aaedc;
    --white: #f3f5f8;
  }
  * { margin: 0; padding: 0; box-sizing: border-box; }
  html, body { width: 1200px; height: 874px; overflow: hidden; }
  body {
    background: var(--backdrop);
    font-family: "Mulish", sans-serif;
    display: flex; flex-direction: column; align-items: center; justify-content: center;
    gap: 30px;
  }
  .card {
    position: relative;
    width: 620px; height: 354px;
    background: var(--navy);
    overflow: hidden;
  }
  /* Back card */
  .brand-lockup {
    position: absolute; inset: 0;
    display: flex; align-items: center; justify-content: center;
  }
  .brand-name {
    color: var(--sky);
    font-size: 54px; font-weight: 400; letter-spacing: 6px;
  }
  /* Front card */
  .identity {
    position: absolute; right: 370px; top: 138px;
    text-align: right;
  }
  .person-name {
    color: var(--orange); font-weight: 700; font-size: 23px; letter-spacing: 0.5px;
    text-transform: uppercase; line-height: 1.1;
  }
  .person-title { color: var(--sky); font-size: 16px; line-height: 1.2; }
  .divider {
    position: absolute; left: 268px; top: 150px;
    width: 1px; height: 80px; background: var(--sky); opacity: .6;
  }
  .contact-list {
    position: absolute; left: 282px; top: 160px;
    list-style: none; color: var(--white); font-size: 14.5px; line-height: 19px;
  }
  .contact-list li { display: flex; align-items: center; gap: 8px; }
  .contact-list svg { width: 11px; height: 11px; fill: var(--orange); flex: none; }
  .address {
    position: absolute; left: 110px; top: 262px;
    color: var(--white); font-size: 15px;
  }
  .band { position: absolute; bottom: 0; height: 13px; }
  .band-sky { left: 0; width: 310px; background: var(--sky); }
  .band-orange { left: 310px; width: 310px; background: var(--orange); }
  .corner-name {
    position: absolute; right: 22px; bottom: 30px;
    color: var(--sky); font-size: 14px; letter-spacing: 2px;
  }
</style>
</head>
<body>
  <section class="card card-back">
    <div class="brand-lockup"><span class="brand-name">RW HOLLIS LLC</span></div>
  </section>

  <section class="card card-front">
    <div class="identity">
      <p class="person-name">Daniel Reyes</p>
      <p class="person-title">President</p>
    </div>
    <div class="divider"></div>
    <ul class="contact-list">
      <li><svg viewBox="0 0 24 24"><path d="M6.6 10.8a15 15 0 0 0 6.6 6.6l2.2-2.2a1 1 0 0 1 1-.25 11.4 11.4 0 0 0 3.6.6 1 1 0 0 1 1 1V20a1 1 0 0 1-1 1A17 17 0 0 1 3 4a1 1 0 0 1 1-1h3.5a1 1 0 0 1 1 1c0 1.25.2 2.45.6 3.6a1 1 0 0 1-.25 1z"/></svg>210-555-0147</li>
      <li><svg viewBox="0 0 24 24"><path d="M7 1h10a2 2 0 0 1 2 2v18a2 2 0 0 1-2 2H7a2 2 0 0 1-2-2V3a2 2 0 0 1 2-2zm0 3v15h10V4z"/></svg>210-555-0193</li>
      <li><svg viewBox="0 0 24 24"><path d="M2 5h20v14H2zm2 2v.5l8 5 8-5V7z"/></svg>reyes@rwhollis.com</li>
      <li><svg viewBox="0 0 24 24"><circle cx="12" cy="12" r="10"/></svg>www.rwhollis.com</li>
    </ul>
    <p class="address">1420 Cedar Ridge Drive, San Antonio, Texas 78205</p>
    <span class="corner-name">RW HOLLIS</span>
    <div class="band band-sky"></div>
    <div class="band band-orange"></div>
  </section>
</body>
</html>
```